Morden, Creative, Unique, Independent Wine Shop

1. We are a brand new wine shop located in Melbourne Australia, we have our logo already, simply use the logo to design a business card.
2. I have uploaded our logo in two versions, with or without shadow, any of them is acceptable.
3. Make it as creative and unique as possible, no limitation of shape, color combination, geometry pattern, fonts, composing etc.
3. Info on the card:
- Brambleford Wine Cellar (Not very necessary if logo is obviously shown)
- 42 Ferncastle Steet, Hampton, Victoria, Australia 3188
- +61 3 9018 4637
- www.bramblefordwinecellar.com.au
- bramblefordwinecellar@mailvista.com
- Additional icons: Google, Snapframe, Friendwall, Chirpline
4. Once again, forget it is a commercial card, make it special.

```html
<!DOCTYPE html>
<html lang="en">
<head>
<meta charset="utf-8">
<title>Brambleford Wine Cellar – Business Card</title>
<link href="https://fonts.googleapis.com/css2?family=Lato:wght@400;700&family=Open+Sans:wght@600&display=swap" rel="stylesheet">
<style>
  :root {
    --backdrop: #1a1a1a;
    --card: #222222;
    --card-edge: #2c2c2c;
    --ink: #ffffff;
    --ink-soft: #e6e6e6;
  }
  * { margin: 0; padding: 0; box-sizing: border-box; }
  html, body {
    width: 1200px; height: 900px; overflow: hidden;
    background: var(--backdrop);
  }
  .stage {
    position: relative; width: 1200px; height: 900px;
  }
  .card {
    position: absolute; left: 290px; width: 620px; height: 355px;
    background: linear-gradient(135deg, var(--card-edge) 0%, var(--card) 55%, #1e1e1e 100%);
    box-shadow: 0 14px 30px rgba(0,0,0,0.6);
    color: var(--ink);
    font-family: "Lato", sans-serif;
  }
  .card--front { top: 60px; }
  .card--back { top: 475px; }

  /* front */
  .brand {
    position: absolute; left: 0; top: 0; width: 100%; height: 100%;
    display: flex; align-items: center; justify-content: center; gap: 18px;
  }
  .brand__dot {
    width: 64px; height: 64px; border: 3px solid var(--ink); border-radius: 50%;
  }
  .brand__name {
    font-family: "Lato", sans-serif; font-weight: 400; color: var(--ink);
    text-transform: uppercase; line-height: 1.15;
  }
  .brand__name-main { display: block; font-size: 40px; letter-spacing: 1px; }
  .brand__name-sub { display: block; font-size: 17px; letter-spacing: 4px; text-align: center; }

  /* back */
  .person {
    position: absolute; left: 40px; top: 128px; width: 235px; text-align: right;
  }
  .person__name {
    font-family: "Open Sans", sans-serif; font-weight: 600;
    font-size: 27px; letter-spacing: 2px; text-transform: uppercase;
    white-space: nowrap;
  }
  .person__role { font-size: 15px; color: var(--ink-soft); margin-top: 2px; }
  .divider {
    position: absolute; left: 292px; top: 122px; width: 1.5px; height: 112px;
    background: var(--ink);
  }
  .contact {
    position: absolute; left: 312px; top: 118px; list-style: none;
    font-size: 15px; line-height: 1.45; color: var(--ink);
  }
  .contact li { display: flex; align-items: center; gap: 8px; }
  .contact__address { padding-left: 0; margin-bottom: 2px; }
  .contact svg { width: 11px; height: 11px; flex: none; fill: none; stroke: var(--ink); stroke-width: 1.6; }
  .social {
    position: absolute; left: 0; width: 100%; top: 296px;
    display: flex; justify-content: center; gap: 20px;
    font-size: 12px; color: var(--ink); list-style: none;
  }
  .social li { display: flex; align-items: center; gap: 5px; }
  .social li::before {
    content: ""; width: 8px; height: 8px; border-radius: 50%; background: var(--ink);
  }
</style>
</head>
<body>
<main class="stage">
  <section class="card card--front" aria-label="Card front">
    <div class="brand">
      <span class="brand__dot" aria-hidden="true"></span>
      <h1 class="brand__name">
        <span class="brand__name-main">Brambleford</span>
        <span class="brand__name-sub">Wine Cellar</span>
      </h1>
    </div>
  </section>

  <section class="card card--back" aria-label="Card back">
    <div class="person">
      <p class="person__name">Daniel Harrow</p>
      <p class="person__role">Director</p>
    </div>
    <span class="divider" aria-hidden="true"></span>
    <ul class="contact">
      <li class="contact__address">42 Ferncastle Steet, Hampton,<br>Victoria, Australia 3188</li>
      <li>
        <svg viewBox="0 0 12 12" aria-hidden="true"><path d="M3 1 L5 3.5 L4 5 Q5 7 7 8 L8.5 7 L11 9 L9.5 11 Q5 10.5 1 3 Z"/></svg>
        +61 3 9018 4637
      </li>
      <li>
        <svg viewBox="0 0 12 12" aria-hidden="true"><rect x="1" y="2.5" width="10" height="7"/><path d="M1 2.5 L6 6.5 L11 2.5"/></svg>
        bramblefordwinecellar@mailvista.com
      </li>
      <li>
        <svg viewBox="0 0 12 12" aria-hidden="true"><circle cx="6" cy="6" r="5"/><path d="M1 6 H11 M6 1 Q3 6 6 11 M6 1 Q9 6 6 11"/></svg>
        www.bramblefordwinecellar.com.au
      </li>
    </ul>
    <ul class="social">
      <li>Circlet</li>
      <li>Snapframe</li>
      <li>Friendwall</li>
      <li>Chirpline</li>
    </ul>
  </section>
</main>
</body>
</html>
```